UTV Ridgemart Website Redesign

I am seeking an eye-catching design for a UTV Wholesale parts website (utvridgemart.com). I have made an initial attempt, but I lack the design expertise to achieve the desired look.
I would like the designers to consider the following website styles when creating the new design:
-UTVkestrel.com: This is the go to website for UTV parts and it has a great design, layout, speed, and product line.
-Fenmoto.com: This site is not a UTV website; however, it is a design that I find to be very appealing and along the lines of what i am looking for.
For temporary use, please use products and product categories you see on https://www.utvbranlo.com/
I have added my own logo to the contest, please use it in your design. I like the use of yellow within the color scheme to match my logo. However, i dont like the all black background that i ended up with on the current version of my site. So i would like something more like fenmoto.com and utvkestrel, where there are some darker colors used but not a full on black background.
Make sure you add in a vehicle year make and model selection tool somewhere at the top of the page
Make sure there is a megamenu with graphical category selections, like you see on the example websites.

```html
<!DOCTYPE html>
<html lang="en">
<head>
<meta charset="utf-8">
<title>UTV Ridgemart</title>
<link href="https://fonts.googleapis.com/css2?family=Roboto:wght@400;500;700&family=Lato:ital,wght@0,400;0,700;1,400&display=swap" rel="stylesheet">
<style>
:root{
  --yellow:#f7df16;
  --yellow-deep:#e9cf00;
  --ink:#1b1b1b;
  --dark:#222222;
  --olive:#3d3a17;
  --grey:#f1f1f1;
  --line:#dddddd;
  --muted:#666666;
  --red:#d24b2a;
  --price:#e3b800;
}
*{box-sizing:border-box;margin:0;padding:0}
html,body{width:1200px;height:4781px;overflow:hidden}
body{position:relative;font-family:"Lato",sans-serif;color:var(--ink);background:#fff}
.abs{position:absolute}
.wrap{position:absolute;left:111px;width:978px}
h1,h2,h3,.heading{font-family:"Roboto",sans-serif}

/* top bar */
.topbar{top:0;left:0;width:1200px;height:34px;background:var(--ink);color:#fff;font:14px/34px "Roboto",sans-serif;text-align:center}
/* header */
.header{top:34px;left:0;width:1200px;height:99px;border-bottom:1px solid var(--line)}
.logo{position:absolute;left:111px;top:30px;display:flex;align-items:center;gap:10px;font:700 30px "Roboto",sans-serif;color:var(--ink)}
.logo-mark{width:34px;height:34px;background:var(--yellow)}
.search{position:absolute;left:450px;top:22px;width:436px;height:54px;border:1px solid #bbb;border-radius:6px;font:15px/52px "Lato",sans-serif;color:#777;padding:0 18px}
.search svg{position:absolute;right:16px;top:17px}
.header-icons{position:absolute;left:978px;top:38px;display:flex;gap:18px}
/* nav */
.nav{top:133px;left:111px;height:53px;display:flex;gap:26px;font:500 16px/53px "Roboto",sans-serif}
.nav .on{color:var(--yellow-deep)}
/* vehicle bar */
.vehicle{top:186px;left:0;width:1200px;height:90px;background:var(--olive)}
.vehicle .label{position:absolute;left:111px;top:0;color:#fff;font:700 20px/90px "Roboto",sans-serif}
.sel{position:absolute;top:21px;height:48px;border:1px solid #d8d4a8;border-radius:4px;color:#fff;font:16px/46px "Roboto",sans-serif;padding-left:16px}
.sel svg{position:absolute;right:14px;top:18px}
.go{position:absolute;left:1038px;top:21px;width:72px;height:48px;background:var(--yellow);border-radius:6px;text-align:center;font:700 18px/48px "Roboto",sans-serif}
/* hero */
.hero{top:276px;left:0;width:1200px;height:457px;background:var(--yellow);overflow:hidden}
.hero-photo{position:absolute;left:0;top:0;width:1200px;height:457px}
.hero .kicker{position:absolute;left:108px;top:48px;font-size:22px}
.hero h1{position:absolute;left:108px;top:96px;font-size:50px;line-height:61px;font-weight:700}
.btn-outline{position:absolute;left:112px;top:310px;width:236px;height:66px;border:2px solid var(--ink);border-radius:6px;font:500 20px/62px "Roboto",sans-serif;text-align:center}
.arrows{position:absolute;display:flex;gap:12px}
.arrow{width:42px;height:42px;border-radius:50%;display:flex;align-items:center;justify-content:center}
/* deals */
.section-title{position:absolute;left:0;width:1200px;text-align:center;font:700 40px "Roboto",sans-serif}
.deals{top:900px;display:grid;grid-template-columns:repeat(4,1fr);gap:20px}
.card{height:376px;border:1px solid var(--line);border-radius:6px;position:relative;background:#fff}
.card.featured{border:2px solid var(--yellow)}
.card .pic{position:absolute;left:16px;right:16px;top:14px;height:172px;border-bottom:1px solid var(--line)}
.card .badge{position:absolute;right:8px;top:16px;background:var(--yellow);border-radius:4px;font:700 14px "Roboto",sans-serif;padding:3px 6px}
.card .name{position:absolute;top:216px;left:10px;right:10px;text-align:center;font:16px/22px "Roboto",sans-serif}
.card .price{position:absolute;top:272px;width:100%;text-align:center;font:17px "Roboto",sans-serif}
.card .price s{color:var(--muted);margin-right:14px}
.card .price b{color:var(--price);font-weight:500}
.card .cta{position:absolute;top:322px;left:50%;transform:translateX(-50%);display:flex;white-space:nowrap}
.cta .add{background:var(--yellow);font:500 16px/40px "Roboto",sans-serif;padding:0 14px;height:40px;border-radius:4px 0 0 4px;white-space:nowrap}
.cta .fav{width:38px;height:40px;background:var(--ink);border-radius:0 4px 4px 0;display:flex;align-items:center;justify-content:center}
/* categories */
.grey{top:1354px;left:0;width:1200px;height:909px;background:var(--grey)}
.tabs{top:1479px;display:flex;justify-content:space-between;font:18px "Roboto",sans-serif}
.tabs .on{border-bottom:3px solid var(--yellow);padding-bottom:6px}
.cats{display:grid;grid-template-columns:repeat(4,1fr);column-gap:20px}
.cat .tile{height:223px;background:#fff}
.cat .lbl{text-align:center;font:500 20px "Roboto",sans-serif;margin-top:22px}
/* promo */
.promo{position:absolute;border-radius:2px;color:#fff;text-align:center;font:700 18px/26px "Roboto",sans-serif;display:flex;flex-direction:column;align-items:center;justify-content:center;gap:16px;padding:0 14px}
.btn-y{background:var(--yellow);color:var(--ink);font:500 18px/44px "Roboto",sans-serif;padding:0 16px;height:44px;border-radius:6px;white-space:nowrap}
/* about */
.about{top:2922px;left:0;width:1200px;height:560px;background:linear-gradient(90deg,#151515 0%,#232323 45%,#4a4236 70%,#8a7a5e 100%)}
.about h2{position:absolute;left:111px;top:112px;color:#fff;font-size:42px;font-weight:700}
.about p{position:absolute;left:111px;top:188px;width:550px;color:#ddd;font-size:16px;line-height:28px}
.about .btn-y{position:absolute;left:111px;top:402px}
/* reviews */
.reviews{top:3450px;left:0;width:1200px;height:530px;background:var(--yellow)}
.badge-circle{position:absolute;left:96px;top:158px;width:316px;height:316px;border-radius:50%;background:#fff;text-align:center}
.stars{color:#e2a10d;letter-spacing:2px}
.review{position:absolute;top:186px;width:320px;font-size:15px;line-height:24px}
.review .who{font:500 18px "Roboto",sans-serif;margin-bottom:16px}
.review .who span{color:var(--red);margin-left:8px}
.review q{font-style:italic;color:#333;display:block}
.review .when{margin-top:20px;color:#333}
/* signup */
.signup-sub{position:absolute;left:0;width:1200px;top:4134px;text-align:center;font-size:18px;color:#444}
.field{position:absolute;left:260px;top:4192px;width:680px;height:60px;border:1px solid #bbb;border-radius:6px;overflow:hidden}
.field span{position:absolute;left:22px;top:0;font:16px/58px "Lato",sans-serif;color:#555}
.field b{position:absolute;right:0;top:0;width:130px;height:58px;background:var(--yellow);text-align:center;font:500 18px/58px "Roboto",sans-serif}
/* footer */
.footer{top:4322px;left:0;width:1200px;height:459px;background:var(--dark);color:#fff}
.social{position:absolute;left:111px;top:114px;display:flex;gap:10px}
.social i{width:50px;height:50px;border:2px solid var(--yellow);border-radius:50%;display:block}
.footer .about-txt{position:absolute;left:111px;top:196px;width:300px;font-size:15px;line-height:22px;color:#ddd}
.fcol{position:absolute;top:92px;font-size:15px;line-height:26px;color:#ddd}
.fcol h4{font:500 22px "Roboto",sans-serif;color:#fff;margin-bottom:16px}
.contact-row{display:flex;gap:10px;margin-bottom:26px}
.copy{position:absolute;left:0;width:1200px;top:394px;border-top:1px solid #444;padding-top:14px;text-align:center;font-size:15px;color:#ddd}
</style>
</head>
<body>

<div class="abs topbar">Summer sale discount off <b>10%!</b> Shop Now</div>

<header class="abs header">
  <div class="logo"><span class="logo-mark"></span>UTV Ridgemart</div>
  <div class="search">Search for products
    <svg width="18" height="18" viewBox="0 0 18 18"><circle cx="7.5" cy="7.5" r="5.5" fill="none" stroke="#222" stroke-width="2"/><path d="M12 12l4.5 4.5" stroke="#222" stroke-width="2"/></svg>
  </div>
  <div class="header-icons">
    <svg width="24" height="22" viewBox="0 0 24 22"><path d="M12 20S2 13.5 2 7.5A5 5 0 0 1 12 5a5 5 0 0 1 10 2.5C22 13.5 12 20 12 20z" fill="none" stroke="#222" stroke-width="2"/></svg>
    <svg width="22" height="22" viewBox="0 0 22 22"><circle cx="11" cy="7" r="5" fill="none" stroke="#222" stroke-width="2"/><path d="M2 21c1-5 5-7 9-7s8 2 9 7" fill="none" stroke="#222" stroke-width="2"/></svg>
    <svg width="30" height="26" viewBox="0 0 30 26"><path d="M1 4h5l3 12h14l3-9H8" fill="none" stroke="#222" stroke-width="2"/><circle cx="11" cy="21" r="2" fill="#222"/><circle cx="21" cy="21" r="2" fill="#222"/><circle cx="26" cy="4" r="4" fill="#f7df16"/></svg>
  </div>
</header>

<nav class="abs nav">
  <span class="on">Home</span><span>Exterior</span><span>Interior</span><span>Wheels &amp; Tires</span><span>Performance</span><span>Suspension</span><span>Steering</span><span>Enhancements</span><span>Misc.</span><span>Sale</span>
</nav>

<section class="abs vehicle">
  <div class="label">SHOP BY VEHICLE</div>
  <div class="sel" style="left:311px;width:228px">Year<svg width="12" height="8" viewBox="0 0 12 8"><path d="M1 1l5 5 5-5" fill="none" stroke="#fff" stroke-width="2"/></svg></div>
  <div class="sel" style="left:553px;width:228px">Make<svg width="12" height="8" viewBox="0 0 12 8"><path d="M1 1l5 5 5-5" fill="none" stroke="#fff" stroke-width="2"/></svg></div>
  <div class="sel" style="left:796px;width:228px">Model<svg width="12" height="8" viewBox="0 0 12 8"><path d="M1 1l5 5 5-5" fill="none" stroke="#fff" stroke-width="2"/></svg></div>
  <div class="go">GO</div>
</section>

<section class="abs hero">
  <svg class="hero-photo" viewBox="0 0 1200 457" role="img" aria-label="Off-road UTV with bright underglow lights driving across desert sand dunes at dusk">
    <defs><linearGradient id="heroG" x1="0" y1="0" x2="0" y2="1"><stop offset="0" stop-color="#2c2a24"/><stop offset=".5" stop-color="#6e5a44"/><stop offset="1" stop-color="#b08c6c"/></linearGradient></defs>
    <path d="M470 0H1200V457H430L445 420 430 380 455 340 440 300 470 260 450 220 480 180 460 140 490 100 470 60 495 30Z" fill="url(#heroG)"/>
  </svg>
  <div class="kicker">Lets take car servicing seriously</div>
  <h1>Full Satisfaction<br>in Affordable<br>Prices</h1>
  <div class="btn-outline">EXPLORE PRODUCTS</div>
  <div class="arrows" style="left:990px;top:326px">
    <div class="arrow" style="background:#222"><svg width="10" height="14" viewBox="0 0 10 14"><path d="M8 1L2 7l6 6" fill="none" stroke="#fff" stroke-width="2"/></svg></div>
    <div class="arrow" style="background:#222"><svg width="10" height="14" viewBox="0 0 10 14"><path d="M2 1l6 6-6 6" fill="none" stroke="#fff" stroke-width="2"/></svg></div>
  </div>
</section>

<h2 class="section-title" style="top:802px">Daily Deal Of The Day</h2>
<div class="wrap deals">
  <div class="card"><div class="pic" role="img" aria-label="Black aluminum camera holder clamp" style="background:radial-gradient(circle at 50% 50%,#555 0,#fff 55%)"></div><span class="badge">-38%</span>
    <div class="name">1.75-2" UTV Pro<br>Aluminum Camera Holder</div><div class="price"><s>$129.99</s><b>$79.99</b></div>
    <div class="cta"><span class="add">ADD TO CART</span><span class="fav"><svg width="16" height="14" viewBox="0 0 16 14"><path d="M8 13S1 8.5 1 4.5A3.5 3.5 0 0 1 8 3a3.5 3.5 0 0 1 7 1.5C15 8.5 8 13 8 13z" fill="#fff"/></svg></span></div></div>
  <div class="card featured"><div class="pic" role="img" aria-label="Black grab bar handle" style="background:radial-gradient(ellipse 20% 45% at 50% 50%,#333 0,#fff 100%)"></div><span class="badge">-38%</span>
    <div class="name">Grab Bar Handle For Utv<br>For Quad Gear,..</div><div class="price"><s>$35.00</s><b>$23.00</b></div>
    <div class="cta"><span class="add">ADD TO CART</span><span class="fav"><svg width="16" height="14" viewBox="0 0 16 14"><path d="M8 13S1 8.5 1 4.5A3.5 3.5 0 0 1 8 3a3.5 3.5 0 0 1 7 1.5C15 8.5 8 13 8 13z" fill="#fff"/></svg></span></div></div>
  <div class="card"><div class="pic" role="img" aria-label="Blue and black waterproof overhead storage bag" style="background:radial-gradient(ellipse 28% 45% at 50% 50%,#2a3550 0,#fff 100%)"></div><span class="badge">-38%</span>
    <div class="name">Waterproof Overhead<br>Storage Bag Overhead..</div><div class="price"><s>$129.99</s><b>$79.99</b></div>
    <div class="cta"><span class="add">ADD TO CART</span><span class="fav"><svg width="16" height="14" viewBox="0 0 16 14"><path d="M8 13S1 8.5 1 4.5A3.5 3.5 0 0 1 8 3a3.5 3.5 0 0 1 7 1.5C15 8.5 8 13 8 13z" fill="#fff"/></svg></span></div></div>
  <div class="card"><div class="pic" role="img" aria-label="Fire extinguisher quick-release mount" style="background:radial-gradient(ellipse 40% 30% at 50% 50%,#444 0,#fff 100%)"></div><span class="badge">-38%</span>
    <div class="name">For Moto Utv Atv Vehicle<br>Mounted Fire Extinguisher</div><div class="price"><s>$129.99</s><b>$79.99</b></div>
    <div class="cta"><span class="add">ADD TO CART</span><span class="fav"><svg width="16" height="14" viewBox="0 0 16 14"><path d="M8 13S1 8.5 1 4.5A3.5 3.5 0 0 1 8 3a3.5 3.5 0 0 1 7 1.5C15 8.5 8 13 8 13z" fill="#fff"/></svg></span></div></div>
</div>

<section class="abs grey">
  <svg class="abs" style="top:-20px;left:0" width="1200" height="40" viewBox="0 0 1200 40"><path d="M0 28L60 16 110 30 180 12 250 26 320 14 400 30 470 18 560 32 640 14 720 28 800 12 880 26 960 16 1040 30 1120 14 1200 24V40H0Z" fill="#f1f1f1"/></svg>
  <svg class="abs" style="bottom:-20px;left:0" width="1200" height="40" viewBox="0 0 1200 40"><path d="M0 0H1200V14L1130 28 1060 12 980 26 900 14 820 30 740 16 660 28 580 12 500 26 420 14 340 30 260 16 180 28 100 12 40 24 0 14Z" fill="#f1f1f1"/></svg>
</section>
<div class="wrap tabs"><span>Exterior</span><span>Interior</span><span class="on">Wheels &amp; Tires</span><span>Lighting</span><span>Performance</span><span>Steering</span><span>Enhancements</span><span>Suspension</span><span>Accessories</span></div>
<div class="wrap cats" style="top:1571px">
  <div class="cat"><div class="tile" role="img" aria-label="Black lug nuts" style="background:radial-gradient(ellipse 40% 30% at 50% 50%,#3a3a3a 0,#fff 100%)"></div><div class="lbl">Lug Nuts</div></div>
  <div class="cat"><div class="tile" role="img" aria-label="Off-road tire with red rim" style="background:radial-gradient(circle at 50% 50%,#5a2222 0,#333 25%,#fff 45%)"></div><div class="lbl">Tires</div></div>
  <div class="cat"><div class="tile" role="img" aria-label="Silver wheel adapters with bolts" style="background:radial-gradient(ellipse 40% 35% at 45% 50%,#9a9a9a 0,#fff 100%)"></div><div class="lbl">Wheel Adapters</div></div>
  <div class="cat"><div class="tile" role="img" aria-label="Black wheel center cap" style="background:radial-gradient(circle at 50% 50%,#2a2a2a 0,#2a2a2a 30%,#fff 42%)"></div><div class="lbl">Wheel Caps</div></div>
</div>
<div class="wrap cats" style="top:1888px">
  <div class="cat"><div class="tile" role="img" aria-label="Wheel spacer with studs" style="background:radial-gradient(circle at 50% 50%,#8a8a8a 0,#fff 45%)"></div><div class="lbl">Wheel Spacers</div></div>
  <div class="cat"><div class="tile" role="img" aria-label="Chrome wheel studs" style="background:radial-gradient(ellipse 40% 25% at 50% 50%,#aaa 0,#fff 100%)"></div><div class="lbl">Wheel Studs</div></div>
  <div class="cat"><div class="tile" role="img" aria-label="Tire repair kit with tools" style="background:radial-gradient(ellipse 42% 22% at 50% 45%,#d2691e 0,#fff 100%)"></div><div class="lbl">Tire Kits</div></div>
  <div class="cat"><div class="tile" role="img" aria-label="Mounted black off-road wheel" style="background:radial-gradient(circle at 50% 50%,#555 0,#222 30%,#fff 44%)"></div><div class="lbl">Pre-Mounted Wheel</div></div>
</div>

<div class="promo" role="img" aria-label="Illuminated rocker switch photo" style="left:111px;top:2352px;width:249px;height:230px;background:linear-gradient(135deg,#1a1a1a,#555 70%,#bbb)">Rocker Switch Horn DC12-24V Illuminated LED WINCH Rear Front lights<span class="btn-y">SHOP NOW!</span></div>
<div class="promo" role="img" aria-label="LED light bar on UTV grille at night" style="left:111px;top:2600px;width:249px;height:231px;background:linear-gradient(160deg,#123040,#1a1a1a 50%,#a55a10)">11" LED Light Bar Bracket Kit Front Grille 60W Front Lamp Bar 6000K 3000K<span class="btn-y">SHOP NOW!</span></div>
<div class="promo" role="img" aria-label="Red lit UTV lighting background" style="left:378px;top:2352px;width:445px;height:479px;background:linear-gradient(180deg,#2a0a0c,#6a1018 60%,#3a0808);font-size:38px;line-height:48px;gap:26px">
  <span style="font-size:30px">UTV Ridgemart</span><span>Premium Lighting<br>Products</span><span class="btn-y">SHOP NOW!</span></div>
<div class="promo" role="img" aria-label="UTV front LED signal lights" style="left:841px;top:2352px;width:248px;height:230px;background:linear-gradient(135deg,#3a2a10,#1a1a1a 50%,#6a5a30)">Front LED Signal Signature Lights for Crestline Vantage X3 XDS XRS<span class="btn-y">SHOP NOW!</span></div>
<div class="promo" role="img" aria-label="UTV roll bar with LED light" style="left:841px;top:2600px;width:248px;height:231px;background:linear-gradient(135deg,#2a2a2a,#505050 50%,#7a4a20)">For Crestline Vantage X3 Universal Roll Bar LED Light UTV ATV For Tallpine<span class="btn-y">SHOP NOW!</span></div>

<section class="abs about">
  <svg class="abs" style="left:560px;top:0" width="640" height="560" viewBox="0 0 640 560" role="img" aria-label="Rider in a white sport UTV kicking up dust on a dirt trail"><defs><radialGradient id="utvG" cx=".45" cy=".55" r=".55"><stop offset="0" stop-color="#e8e8e8"/><stop offset=".45" stop-color="#555"/><stop offset="1" stop-color="#000" stop-opacity="0"/></radialGradient></defs><ellipse cx="290" cy="300" rx="300" ry="250" fill="url(#utvG)"/></svg>
  <svg class="abs" style="top:-18px;left:0" width="1200" height="36" viewBox="0 0 1200 36"><path d="M0 0H1200V10L1120 24 1040 8 960 22 880 10 800 26 720 12 640 24 560 8 480 22 400 10 320 26 240 12 160 24 80 10 0 22Z" fill="#fff"/></svg>
  <h2>About UTV Ridgemart</h2>
  <p>Lorem ipsum dolor sit amet, consectetur adipiscing elit, sed do eiusmod tempor incididunt ut labore et dolore magna aliqua. Ut enim ad minim veniam, quis nos trud exercitation ullamco laboris nisi ut aliquip ex ea commodo consequat. Duis aute irure dolor in repreh kienderit in volu ptate velit esse cillum dolore eu fugiat nulla pariatur. Excepteur sint occ aecat cupidatat non pro ident unt in culp.</p>
  <span class="btn-y">SHOP NOW!</span>
</section>

<section class="abs reviews">
  <svg class="abs" style="top:-14px;left:0" width="1200" height="40" viewBox="0 0 1200 40"><path d="M0 20L70 8 150 24 230 6 320 22 400 10 480 26 560 12 640 24 720 8 800 22 880 12 960 26 1040 10 1120 22 1200 12V40H0Z" fill="#f7df16"/></svg>
  <div class="badge-circle">
    <div class="heading" style="font-size:40px;font-weight:700;margin-top:40px">Reviews</div>
    <div class="stars" style="font-size:28px;margin-top:6px">★★★★★</div>
    <div class="heading" style="font-size:24px;font-weight:500;margin-top:6px">Excellent</div>
    <div style="font-size:15px;margin-top:12px;color:#444">4.62 Average &nbsp;|&nbsp; 5772 Reviews</div>
    <div style="font-size:24px;margin-top:16px;display:flex;justify-content:center;align-items:center;gap:6px"><span style="width:20px;height:20px;border-radius:50%;background:#222;display:inline-block"></span>ReviewNest</div>
  </div>
  <div class="review" style="left:447px"><div class="who">Anonymous<span>★★★★★</span></div><q>Nemo enim ipsam voluptatem quia volulp tas sit aspernatur aut odit aut fugit, sed qui a consequuntur magni dolores eos qui rati one voluptatem sequi nesciunt.</q><div class="when">Posted 2 weeks ago</div></div>
  <div class="review" style="left:807px"><div class="who">Anonymous<span>★★★★★</span></div><q>Nemo enim ipsam voluptatem quia volulp tas sit aspernatur aut odit aut fugit, sed qui a consequuntur magni dolores eos qui rati one voluptatem sequi nesciunt.</q><div class="when">Posted 2 weeks ago</div></div>
  <div class="arrows" style="left:988px;top:432px">
    <div class="arrow" style="background:#f0c400"><svg width="10" height="14" viewBox="0 0 10 14"><path d="M8 1L2 7l6 6" fill="none" stroke="#fff" stroke-width="2"/></svg></div>
    <div class="arrow" style="background:#f0c400"><svg width="10" height="14" viewBox="0 0 10 14"><path d="M2 1l6 6-6 6" fill="none" stroke="#fff" stroke-width="2"/></svg></div>
  </div>
  <svg class="abs" style="bottom:-12px;left:0" width="1200" height="30" viewBox="0 0 1200 30"><path d="M0 0H1200V10L1100 20 1000 6 900 18 800 8 700 22 600 8 500 20 400 6 300 18 200 8 100 22 0 10Z" fill="#f7df16"/></svg>
</section>

<h2 class="section-title" style="top:4068px;font-size:38px;font-weight:500">Sign Up and Save</h2>
<div class="signup-sub">Exclusive email offers &amp; Limited time</div>
<div class="field"><span>Email address</span><b>SUBSCRIBE</b></div>

<footer class="abs footer">
  <svg class="abs" style="top:-16px;left:0" width="1200" height="36" viewBox="0 0 1200 36"><path d="M0 22L80 8 160 24 240 10 330 26 410 12 500 24 580 8 660 22 740 10 830 26 910 12 1000 24 1080 8 1200 20V36H0Z" fill="#222"/></svg>
  <div class="social"><i></i><i></i><i></i><i></i><i></i></div>
  <p class="about-txt">uis aute irure dolor in reprehenderit in voluptate velit esse cillum dolore eu fu giat nulla pariatur. Excepteur sint occae cat cupidatat unt in culpa qui officia deserunt mollit anim id.</p>
  <div class="fcol" style="left:456px"><h4>Categories</h4>Body &amp; Exterior<br>Interior &amp; Comfort<br>Wheels &amp; Tires<br>Engine Performance<br>Suspension &amp; Lift Kits<br>Drivetrain &amp; Steering<br>Enhancements &amp; Add-Ons<br>Misc.</div>
  <div class="fcol" style="left:688px"><h4>Policies</h4>Privacy Policy<br>Refund Policy<br>Terms of Service<br>Return Policy</div>
  <div class="fcol" style="left:859px;width:250px"><h4>Contact Us</h4>
    <div class="contact-row"><svg width="12" height="16" viewBox="0 0 12 16" style="margin-top:5px;flex:none"><path d="M6 15S1 9 1 6a5 5 0 0 1 10 0c0 3-5 9-5 9z" fill="#f7df16"/></svg><span>418 Quarry Ridge Rd, Harlow Missouri 65999, United States</span></div>
    <div class="contact-row"><svg width="14" height="12" viewBox="0 0 14 12" style="margin-top:7px;flex:none"><rect width="14" height="11" fill="#f7df16"/><path d="M0 0l7 6 7-6" fill="none" stroke="#222" stroke-width="1.5"/></svg><span>info@utvridgemart.com</span></div>
    <div class="contact-row"><svg width="14" height="14" viewBox="0 0 14 14" style="margin-top:6px;flex:none"><path d="M3 1l3 3-2 2c1 2 2 3 4 4l2-2 3 3-2 2C6 13 1 8 1 3z" fill="#f7df16"/></svg><span>+ 4175550142</span></div>
  </div>
  <div class="copy">Copyright © 2024 UTV Ridgemart.com. All rights reserved.</div>
</footer>

</body>
</html>
```